The Meridale Works
Buy+Sell+Repair & Take trade-ins. New & Used, All makes and models
24 Hours or so left in this contest. We have seen many good designs and a few of you are in contention as you have incorporated what we sell like GPS & Total stations etc which we like. We hope to get some even stronger options with our suggestions in mind in the closing hours but also the sooner the better. If we like your design but would simply like to make a small revision, we would like to give you time to correct prior to us picking another winner. Thanks for all your efforts.
draft #155 We like your creativity! Would like to see some new drafts from you soon showing some of the suggestions mentioned in previous posts. Maybe make the large earth and satellite more translucent. Put dots in between words like buy+sell etc instread of plus signs. Use icons to show quorvel, bramnet, phone, email and Valto then follow with proper info. Move everything around if need be to try to make look clean while having this info available. Look forward to new options from you. Thanks
#162 please make Icons & info larger.
#163 Can you move our logo & company name up a little & put buy, sell ect. just under it in the grey area.
Then put " Dealing in VORANT, MELDRIX, KAPUNO, FELSTOW, & ZIRVAN." in the blue area.
Note Please use period or comma instead of "+" on designs.
Project# 102,
I really like this one. Will you :
1) Take away the "box" from our names & put Names in upper corner, & put "Phone# & Email & address."
2) Keep our logo & company name as is.
3) Bottom left area put " Buy. Sell. Trade. Repair. New & Used. GPS. Robotics. Total Stations. Theodolites. & Levels "
4) Bottom Right area put "Bramnet, Valto, Quorvel, ect." (Please use "Icon" instead of words.)
5)To every one .... I would like to see the package deal after we get the card layout handled. ( I also like some of the ideas of the "swoosh" on the cars but don't know if the "info" will fit rite.
Thank you for your help.
Also please no highlight block over our names
Fifth but very important is that we are primarily an Internet based company and our Address is not really needed on our business card. Addreess could be removed but please include a second email address being dana@themeridaleworks.example to this card.
Fourth, Please keep with the concept I have seen on several designs that puts a translucent version of our globe logo on the opposite side of the darker logo. This more translucent globe can have our company contact info written on top of it as long as it still looks clean and the info is very clear to read.
Third, We like a small swoosh to seperate the card into two halves.
Second I very much need the card to have the logo and our name but then under that it should read Buy+Sell+Repair+Trade-in+New & Used+ All makes and Models. as seen in design #152
This should be a must!
Greeting all,
Sorry that I have not given much feedback yet but things are very busy. I have looked over the designs and have a few suggestions. First I will probably choose a design that gives the whole stationary and envelope options too.

```html
<!DOCTYPE html>
<html lang="en">
<head>
<meta charset="utf-8">
<title>The Meridale Works – Business Card</title>
<link rel="stylesheet" href="https://fonts.googleapis.com/css2?family=Open+Sans:wght@400;700&display=swap">
<style>
  :root {
    --page-bg: #ececec;
    --card-bg: #ffffff;
    --navy: #1c2f6b;
    --blue-deep: #0d1f55;
    --blue-mid: #2c55b8;
    --blue-light: #7fa4e8;
    --text-grey: #6a6f78;
    --rule-grey: #c9ccd2;
    --icon-grey: #8b9099;
  }
  html, body {
    margin: 0;
    width: 1200px;
    height: 780px;
    overflow: hidden;
    background: var(--page-bg);
    font-family: "Open Sans", Arial, sans-serif;
  }
  .business-card {
    position: absolute;
    left: 100px;
    top: 104px;
    width: 1000px;
    height: 572px;
    background: var(--card-bg);
    border-radius: 32px;
    overflow: hidden;
    box-shadow: 0 6px 24px rgba(0,0,0,0.18);
  }
  .card-art {
    position: absolute;
    inset: 0;
  }
  .brand {
    position: absolute;
    left: 50px;
    top: 200px;
    width: 320px;
    text-align: center;
  }
  .brand-mark {
    width: 150px;
    height: 150px;
    margin: 0 auto 14px;
    border-radius: 50%;
    background: radial-gradient(circle at 40% 35%, var(--blue-light), var(--blue-mid) 55%, var(--blue-deep));
  }
  .brand-name {
    margin: 0;
    font-weight: 700;
    font-size: 30px;
    color: var(--navy);
    line-height: 1.1;
  }
  .brand-tagline {
    margin: 12px 0 0;
    font-size: 15px;
    line-height: 1.45;
    color: var(--text-grey);
  }
  .contact {
    position: absolute;
    left: 450px;
    top: 72px;
    color: var(--text-grey);
  }
  .contact-names {
    margin: 0 0 40px;
    font-size: 30px;
    font-weight: 700;
    color: var(--navy);
  }
  .contact-list {
    list-style: none;
    margin: 0;
    padding: 0;
  }
  .contact-item {
    display: flex;
    align-items: center;
    gap: 12px;
    font-size: 18px;
    height: 40px;
    white-space: nowrap;
  }
  .contact-icon {
    width: 22px;
    height: 22px;
    flex: none;
  }
  .contact-icon.network {
    border-radius: 5px;
    background: var(--blue-mid);
  }
</style>
</head>
<body>
  <div class="business-card">
    <svg class="card-art" viewBox="0 0 1000 572" width="1000" height="572" aria-hidden="true">
      <defs>
        <linearGradient id="swoosh-blue" x1="0" y1="0" x2="1" y2="1">
          <stop offset="0" stop-color="#0b1a4a"/>
          <stop offset="0.6" stop-color="#24489e"/>
          <stop offset="1" stop-color="#4d78d0"/>
        </linearGradient>
      </defs>
      <path d="M0,0 H400 C392,110 350,170 290,200 C330,120 300,50 0,38 Z" fill="url(#swoosh-blue)"/>
      <path d="M0,38 C300,50 330,120 290,200 C322,122 290,64 0,58 Z" fill="#a9bde6"/>
      <path d="M1000,370 C975,520 870,560 760,572 H1000 Z" fill="url(#swoosh-blue)"/>
      <path d="M1000,370 C975,520 870,560 760,572 H740 C860,556 968,512 1000,350 Z" fill="#a9bde6"/>
      <path d="M420,70 C440,230 430,400 395,540" fill="none" stroke="var(--rule-grey)" stroke-width="2"/>
    </svg>

    <div class="brand">
      <div class="brand-mark" role="img" aria-label="Company globe emblem"></div>
      <p class="brand-name">The Meridale Works</p>
      <p class="brand-tagline">Buy. Sell. Repair. Trade-in.<br>New &amp; Used. All makes and models.</p>
    </div>

    <div class="contact">
      <h1 class="contact-names">Dana &amp; Rowan Pellick</h1>
      <ul class="contact-list">
        <li class="contact-item">
          <svg class="contact-icon" viewBox="0 0 24 24" aria-hidden="true"><path d="M6.6 10.8a15 15 0 0 0 6.6 6.6l2.2-2.2c.3-.3.7-.4 1-.2 1.1.4 2.3.6 3.6.6.6 0 1 .4 1 1V20c0 .6-.4 1-1 1A17 17 0 0 1 3 4c0-.6.4-1 1-1h3.5c.6 0 1 .4 1 1 0 1.3.2 2.5.6 3.6.1.3 0 .7-.2 1z" fill="var(--icon-grey)"/></svg>
          (555) 014-2290
        </li>
        <li class="contact-item">
          <svg class="contact-icon" viewBox="0 0 24 24" aria-hidden="true"><rect x="2" y="5" width="20" height="14" rx="2" fill="none" stroke="var(--icon-grey)" stroke-width="2"/><path d="M3 6l9 7 9-7" fill="none" stroke="var(--icon-grey)" stroke-width="2"/></svg>
          rowan@themeridaleworks.example
        </li>
        <li class="contact-item">
          <svg class="contact-icon" viewBox="0 0 24 24" aria-hidden="true"><rect x="2" y="5" width="20" height="14" rx="2" fill="none" stroke="var(--icon-grey)" stroke-width="2"/><path d="M3 6l9 7 9-7" fill="none" stroke="var(--icon-grey)" stroke-width="2"/></svg>
          dana@themeridaleworks.example
        </li>
        <li class="contact-item">
          <span class="contact-icon network" role="img" aria-label="Valto"></span>
          the.meridale.works
        </li>
        <li class="contact-item">
          <span class="contact-icon network" role="img" aria-label="Quorvel"></span>
          Quorvel: @TheMeridaleWorks
        </li>
        <li class="contact-item">
          <span class="contact-icon network" role="img" aria-label="Bramnet"></span>
          pub/rowan-pellick/41/208/c35
        </li>
      </ul>
    </div>
  </div>
</body>
</html>
```